依頼詳細
作成はレスポンシブウェブデザインにて作成をしようと考えているのですが、
SEOにも配慮したデザインを希望してます。

WEBサイトの雰囲気としては
http://lumivane.com/
上記のようなテイストを希望しています。
また、医療機関であり、患者さんがすぐに欲しい情報にたどり着けるよう
http://www.kozuetani-hp.or.jp/
上記のURLのような配置であれば診療時間やアクセスなどにすぐたどり着けて患者さんにとって利便性が高いと考えています。

・基本的に現行のサイトのページは全てリニューアルサイトに盛り込む予定
・基礎的なSEOを考慮して文字に関しては極力テキストで入れることを想定
・レスポンシブウェブデザインを前提としたデザイン

した上で、デザインをお願いできれば幸いです。
サイトURL
http://www.sorvane-dc.jp/
ページ数
2ページ
希望イメージ
シンプル 複雑
単色 カラフル
暗い 明るい
日常 高級
遊び心 厳粛
未来的 伝統的
女性的 男性的
希望する色
白をベースに清潔感かつモダンなイメージ
納品ファイル
• 高解像度JPG (.jpg)
• イラストレーター形式 (.ai)
補足説明

SEOを考えたときにある程度文字を入れるスペースを欲しかったので、そのような部分も確保しつつサイトのデザインが私のイメージに最も近かったので選ばせて頂きました。

皆様からの多数のご応募ありがとうございました。また次の機会もありましたらよろしくお願い致します。

```html
<!DOCTYPE html>
<html lang="ja">
<head>
<meta charset="utf-8">
<title>ソルヴェイン歯科クリニック</title>
<link rel="stylesheet" href="https://fonts.googleapis.com/css2?family=Noto+Sans+JP:wght@400;500;700&family=Roboto:wght@400;700&display=swap">
<style>
:root{
  --green:#3bb391;
  --green-dark:#2e9a7b;
  --ink:#333;
  --muted:#777;
  --dark:#4b4b4b;
  --darker:#3c3c3c;
  --line:#dcdcdc;
  --page:#eeeeee;
  --white:#fff;
}
*{box-sizing:border-box;margin:0;padding:0}
html,body{width:795px;height:1200px;overflow:hidden}
body{background:var(--page);font-family:"Noto Sans JP",sans-serif;color:var(--ink);font-size:8px;line-height:1.5;position:relative}
.topbar{height:22px;background:var(--dark);display:flex;align-items:center;padding-left:21px;gap:14px}
.topbar .tag{background:#e6e6e6;color:var(--dark);font-size:6px;padding:2px 8px;width:160px;text-align:center;font-family:"Roboto",sans-serif;letter-spacing:.5px}
.topbar p{color:#ddd;font-size:6.5px}
.wrap{position:absolute;top:30px;left:21px;width:754px;display:flex;gap:9px}
/* sidebar */
.sidebar{width:160px}
.brand{background:var(--white);height:104px;display:flex;flex-direction:column;align-items:center;justify-content:center;gap:4px}
.brand .catch{font-size:7px;color:var(--muted)}
.brand .mark{width:26px;height:26px;background:var(--dark)}
.brand .name{font-size:10px;font-weight:700;color:var(--dark);font-family:"Roboto",sans-serif;letter-spacing:.5px}
.brand .jp{font-size:6.5px;color:var(--muted)}
.nav{list-style:none;margin-top:2px}
.nav li{background:var(--dark);color:#fff;font-size:8px;height:27px;line-height:27px;padding-left:12px;border-bottom:1px solid #5f5f5f;position:relative}
.nav li::after{content:"";position:absolute;right:10px;top:11px;width:4px;height:4px;border-top:1px solid #aaa;border-right:1px solid #aaa;transform:rotate(45deg)}
.nav li.current{background:var(--darker)}
.side-banner{margin-top:8px;background:var(--white);padding:8px;text-align:center}
.side-banner .lead{font-size:7px;color:var(--muted)}
.side-banner .btn{display:block;background:var(--green);color:#fff;font-size:8px;margin-top:5px;padding:4px 0}
.side-tel{margin-top:8px;background:var(--white);padding:8px;display:flex;align-items:center;gap:6px}
.side-tel .num{font-family:"Roboto",sans-serif;font-weight:700;font-size:15px;color:var(--green)}
.side-tel small{display:block;font-size:6px;color:var(--muted)}
.green-banner{margin-top:8px;background:var(--green);color:#fff;padding:9px 10px;font-size:8px;font-weight:500}
.green-banner span{display:block;font-size:6px;font-weight:400;opacity:.9}
/* main */
.main{width:585px}
.row{display:flex;gap:8px;margin-bottom:8px}
.panel{background:var(--white);padding:9px 10px}
.panel-head{display:flex;justify-content:space-between;align-items:center;border-bottom:1px solid var(--line);padding-bottom:5px;margin-bottom:6px}
.panel-head h2{font-size:8.5px;font-weight:500;border-left:3px solid var(--green);padding-left:5px}
.panel-head .more{background:var(--green);color:#fff;font-size:6px;padding:2px 9px;font-family:"Roboto",sans-serif}
.hero{width:310px;height:120px;background:linear-gradient(135deg,#dfe7ea,#f6f7f7 55%,#cfd9dc);position:relative}
.hero p{position:absolute;bottom:6px;left:8px;right:8px;font-size:6.5px;color:var(--dark)}
.hours{width:267px;height:120px}
.hours table{width:100%;border-collapse:collapse;font-size:6.5px}
.hours td{padding:1.5px 0;color:#555}
.hours .tel{display:flex;align-items:center;gap:5px;margin-top:6px;border-top:1px solid var(--line);padding-top:6px}
.hours .tel b{font-family:"Roboto",sans-serif;font-size:14px;color:var(--green)}
.news{width:288px;height:128px}
.news li{list-style:none;border-bottom:1px dotted var(--line);padding:2px 0;font-size:6.5px}
.news li time{display:block;color:var(--muted);font-size:6px}
.access{width:289px;height:128px}
.map{height:90px;background:linear-gradient(160deg,#e4e8e2,#f2f2ee 50%,#dde3e6)}
.link{font-size:6px;color:var(--muted);text-align:right;margin-top:3px}
.menu{height:655px}
.menu-grid{display:grid;grid-template-columns:1fr 1fr;column-gap:14px;row-gap:10px;margin-top:4px}
.item{display:flex;gap:8px;height:146px;border-bottom:1px solid var(--line);padding:4px 0}
.thumb{width:104px;height:80px;flex:none;background:linear-gradient(135deg,#e3ecee,#c9d6da)}
.item h3{font-size:8.5px;font-weight:500;color:var(--dark);margin-bottom:3px}
.item p{font-size:6.5px;color:#666;line-height:1.55}
.item .link{margin-top:5px}
.to-top{position:absolute;top:966px;left:742px;width:32px;height:32px;background:var(--dark);display:flex;align-items:center;justify-content:center}
/* footer */
.footer{position:absolute;top:1010px;left:0;width:795px;height:190px;background:var(--dark);color:#ddd}
.footer-inner{display:flex;gap:14px;padding:14px 21px 0}
.footer-brand{width:150px;text-align:center}
.footer-brand .mark{width:26px;height:26px;background:#ddd;margin:6px auto 4px}
.footer-brand .name{font-family:"Roboto",sans-serif;font-weight:700;font-size:10px;color:#fff}
.footer-brand .num{font-family:"Roboto",sans-serif;font-weight:700;font-size:15px;color:#fff;margin-top:6px}
.footer-brand small{display:block;font-size:6px;color:#bbb}
.fcol{width:130px}
.fcol h4{font-size:7px;font-weight:500;color:#fff;border-bottom:1px solid #666;padding-bottom:3px;margin-bottom:3px}
.fcol li{list-style:none;font-size:6.5px;color:#ccc;padding:1px 0}
.copy{position:absolute;bottom:0;left:0;right:0;height:18px;background:var(--darker);font-size:6px;color:#aaa;text-align:right;padding:5px 21px}
</style>
</head>
<body>
<header class="topbar">
  <span class="tag">SORVANE DENTAL CLINIC</span>
  <p>ソルヴェイン歯科クリニックは優しい歯科医院です。佐賀市内の皆様の歯の健康を丁寧にお守りします。</p>
</header>

<div class="wrap">
  <aside class="sidebar">
    <div class="brand">
      <span class="catch">佐賀の優しい歯科医院</span>
      <span class="mark"></span>
      <span class="name">SORVANE DENTAL CLINIC</span>
      <span class="jp">ソルヴェイン歯科クリニック</span>
    </div>
    <ul class="nav">
      <li class="current">ホーム</li>
      <li>医院案内</li>
      <li>初めての方へ</li>
      <li>診療案内</li>
      <li>診療時間</li>
      <li>医療設備</li>
      <li>スタッフ紹介</li>
      <li>アクセス</li>
      <li>料金表</li>
    </ul>
    <div class="side-banner">
      <p class="lead">お口のお悩み、ご相談ください</p>
      <span class="btn">初めての方へ</span>
    </div>
    <div class="side-tel">
      <svg width="16" height="16" viewBox="0 0 16 16"><path d="M4 1l3 3-2 2c1 2 3 4 5 5l2-2 3 3-2 3C7 15 1 9 1 4z" fill="#3bb391"/></svg>
      <div><small>ご予約・お問い合わせ</small><span class="num">0952-64-8130</span></div>
    </div>
    <div class="green-banner">無料カウンセリング<span>お気軽にお申し込みください</span></div>
    <div class="green-banner">スタッフ募集<span>一緒に働く仲間を募集中</span></div>
  </aside>

  <main class="main">
    <div class="row">
      <div class="hero" role="img" aria-label="明るい診療室で歯科医が患者の歯を診察する写真">
        <p>清潔で明るい診療室で、患者さまに寄り添った治療を行います。</p>
      </div>
      <section class="panel hours">
        <div class="panel-head"><h2>診療時間</h2><span class="more">MORE</span></div>
        <table>
          <tr><td>午前</td><td>09:00〜13:00（月〜土）</td></tr>
          <tr><td>午後</td><td>14:30〜19:00（土曜は17:00まで）</td></tr>
          <tr><td>休診</td><td>日曜・祝日</td></tr>
        </table>
        <div class="tel">
          <svg width="14" height="14" viewBox="0 0 16 16"><path d="M4 1l3 3-2 2c1 2 3 4 5 5l2-2 3 3-2 3C7 15 1 9 1 4z" fill="#3bb391"/></svg>
          <b>0952-64-8130</b>
        </div>
      </section>
    </div>

    <div class="row">
      <section class="panel news">
        <div class="panel-head"><h2>お知らせ</h2><span class="more">MORE</span></div>
        <ul>
          <li><time>2015.08.01</time>夏季休診日のお知らせを掲載しました。</li>
          <li><time>2015.07.15</time>ホームページをリニューアルいたしました。</li>
          <li><time>2015.07.01</time>土曜日の診療時間が変更になりました。</li>
        </ul>
        <p class="link">一覧はこちら</p>
      </section>
      <section class="panel access">
        <div class="panel-head"><h2>アクセス</h2><span class="more">MORE</span></div>
        <div class="map" role="img" aria-label="医院周辺の地図"></div>
        <p class="link">詳しくはこちら</p>
      </section>
    </div>

    <section class="panel menu">
      <div class="panel-head"><h2>診療メニュー</h2><span class="more">MORE</span></div>
      <div class="menu-grid">
        <article class="item"><div class="thumb" role="img" aria-label="白く輝く歯の写真"></div><div><h3>ホワイトニング</h3><p>歯の表面を傷つけずに、自然な白さを取り戻します。短期間で効果を実感いただけます。</p><p class="link">詳しくはこちら</p></div></article>
        <article class="item"><div class="thumb" role="img" aria-label="インプラント模型の写真"></div><div><h3>インプラント</h3><p>失った歯を補い、自分の歯のように噛める快適さを取り戻す治療です。</p><p class="link">詳しくはこちら</p></div></article>
        <article class="item"><div class="thumb" role="img" aria-label="美しい歯並びの口元の写真"></div><div><h3>審美歯科</h3><p>見た目の美しさと機能を両立し、自信の持てる口元をつくります。</p><p class="link">詳しくはこちら</p></div></article>
        <article class="item"><div class="thumb" role="img" aria-label="歯のクリーニングの写真"></div><div><h3>予防歯科</h3><p>定期検診とクリーニングで、むし歯や歯周病を未然に防ぎます。</p><p class="link">詳しくはこちら</p></div></article>
        <article class="item"><div class="thumb" role="img" aria-label="小児歯科の診療風景の写真"></div><div><h3>小児歯科</h3><p>お子さまが怖がらずに通えるよう、やさしく丁寧に診療します。</p><p class="link">詳しくはこちら</p></div></article>
        <article class="item"><div class="thumb" role="img" aria-label="歯ぐきの検査の写真"></div><div><h3>歯周病</h3><p>歯ぐきの腫れや出血が気になる方は、早めの検査をおすすめします。</p><p class="link">詳しくはこちら</p></div></article>
        <article class="item"><div class="thumb" role="img" aria-label="透明なマウスピースの写真"></div><div><h3>クリアアライナー</h3><p>目立たない透明なマウスピースで、歯並びを整える矯正治療です。</p><p class="link">詳しくはこちら</p></div></article>
        <article class="item"><div class="thumb" role="img" aria-label="あごの診察の写真"></div><div><h3>顎関節症治療</h3><p>あごの痛みや口の開けにくさなど、症状に合わせて治療します。</p><p class="link">詳しくはこちら</p></div></article>
      </div>
    </section>
  </main>
</div>

<div class="to-top"><svg width="14" height="12" viewBox="0 0 14 12"><path d="M7 0l7 8H9v4H5V8H0z" fill="#fff"/></svg></div>

<footer class="footer">
  <div class="footer-inner">
    <div class="footer-brand">
      <small>佐賀の優しい歯科医院</small>
      <div class="mark"></div>
      <div class="name">SORVANE DENTAL CLINIC</div>
      <small>ソルヴェイン歯科クリニック</small>
      <div class="num">0952-64-8130</div>
      <small>佐賀県佐賀市中央町1-2-3</small>
    </div>
    <div class="fcol"><h4>ソルヴェインについて</h4><ul><li>ホーム</li><li>医院案内</li><li>初めての方へ</li><li>診療時間</li><li>医療設備</li><li>スタッフ紹介</li><li>アクセス</li></ul></div>
    <div class="fcol"><h4>診療案内</h4><ul><li>ホワイトニング</li><li>インプラント</li><li>審美歯科</li><li>予防歯科</li><li>小児歯科</li><li>歯周病</li><li>顎関節症治療</li></ul></div>
    <div class="fcol"><h4>その他の情報</h4><ul><li>料金表</li><li>お知らせ</li><li>よくある質問</li><li>スタッフ募集</li></ul></div>
    <div class="fcol"><h4>ご予約・お問い合わせ</h4><ul><li>無料カウンセリング</li><li>お問い合わせ</li><li>プライバシーポリシー</li></ul></div>
  </div>
  <p class="copy">Copyright © 2015 Sorvane Dental Clinic All Rights Reserved.</p>
</footer>
</body>
</html>
```